Stationery Design Project

We need a stationary design for a well-known architect in Guadalajara, Mexico. This architect specializes in very luxurious homes and commercial developments. His clients are very sophisticated, so the letterhead should be equally sophisticated. References to mythology, etc. might be a plus. The letterhead may be embossed and will be printed on a heavy-weight linen. His homes and developments are very luxurious but not necessarily ultra-modern in their aesthetic.
Target Market(s)
High end developers and luxury home buyers
Industry/Entity Type
Architect
Look and feel

```html
<!DOCTYPE html>
<html lang="es">
<head>
<meta charset="utf-8">
<title>Casa Velarde — Membrete</title>
<link rel="stylesheet" href="https://fonts.googleapis.com/css2?family=Montserrat:wght@700&family=Oswald:wght@400&family=Cormorant+Garamond:ital,wght@1,500&display=swap">
<style>
  :root {
    --paper: #ffffff;
    --ink: #000000;
    --bar-top: #4a4a4a;
    --bar-mid: #050505;
    --gold-light: #d8c27a;
    --gold: #b39a55;
    --gold-dark: #6e5a2a;
    --bronze-dark: #4f3d1c;
    --bronze: #8a6a3c;
    --ribbon-text: #e8e8e8;
  }
  html, body {
    margin: 0;
    padding: 0;
    width: 927px;
    height: 1200px;
    overflow: hidden;
    background: var(--paper);
  }
  .letterhead {
    position: relative;
    width: 927px;
    height: 1200px;
    background: var(--paper);
  }
  .header-bar {
    position: absolute;
    top: 118px;
    height: 44px;
    background: linear-gradient(180deg, var(--bar-top) 0%, var(--bar-mid) 18%, var(--bar-mid) 82%, #2a2a2a 100%);
    box-shadow: 0 3px 5px rgba(0,0,0,0.35);
  }
  .header-bar--left { left: 0; width: 360px; border-radius: 0 4px 4px 0; }
  .header-bar--right { left: 562px; width: 365px; border-radius: 4px 0 0 4px; }
  .brand {
    position: absolute;
    top: 40px;
    left: 365px;
    width: 192px;
    height: 200px;
    display: flex;
    flex-direction: column;
    align-items: center;
    justify-content: center;
    gap: 14px;
  }
  .brand__dot {
    width: 54px;
    height: 54px;
    border-radius: 50%;
    background: var(--ink);
  }
  .brand__name {
    font-family: "Montserrat", sans-serif;
    font-weight: 700;
    font-size: 17px;
    letter-spacing: 3px;
    color: var(--gold);
    text-align: center;
    line-height: 1.2;
  }
  .footer-contact {
    position: absolute;
    top: 1108px;
    font-family: "Montserrat", sans-serif;
    font-weight: 700;
    font-size: 14.5px;
    letter-spacing: 4px;
    color: var(--ink);
    line-height: 17px;
    text-align: center;
    white-space: nowrap;
  }
  .footer-contact--street { left: 10px; width: 345px; }
  .footer-contact--city { left: 622px; width: 295px; }
  .footer-phone {
    position: absolute;
    top: 1104px;
    left: 358px;
    width: 258px;
    text-align: center;
    font-family: "Oswald", sans-serif;
    font-size: 22px;
    letter-spacing: 0.5px;
    color: var(--ink);
    white-space: nowrap;
  }
  .footer-rule {
    position: absolute;
    top: 1144px;
    height: 22px;
    background: linear-gradient(180deg, var(--gold-light) 0%, var(--gold) 12%, var(--bronze-dark) 30%, var(--bronze-dark) 80%, var(--gold-dark) 100%);
  }
  .footer-rule--left { left: 0; width: 370px; }
  .footer-rule--right {
    left: 604px;
    width: 323px;
    background: linear-gradient(180deg, var(--gold-light) 0%, var(--gold) 12%, var(--bronze) 30%, var(--bronze) 80%, var(--gold-dark) 100%);
  }
  .ribbon {
    position: absolute;
    top: 1130px;
    left: 354px;
    width: 266px;
    height: 50px;
  }
  .ribbon__label {
    position: absolute;
    top: 1136px;
    left: 354px;
    width: 266px;
    text-align: center;
    font-family: "Cormorant Garamond", serif;
    font-style: italic;
    font-weight: 500;
    font-size: 27px;
    letter-spacing: 4px;
    color: var(--ribbon-text);
  }
</style>
</head>
<body>
<main class="letterhead">
  <header>
    <div class="header-bar header-bar--left"></div>
    <div class="header-bar header-bar--right"></div>
    <div class="brand">
      <div class="brand__dot"></div>
      <div class="brand__name">CASA<br>VELARDE</div>
    </div>
  </header>

  <footer>
    <div class="footer-rule footer-rule--left"></div>
    <div class="footer-rule footer-rule--right"></div>

    <address class="footer-contact footer-contact--street" style="font-style:normal">Paseo de los Olivos #1540<br>Colinas del Sol</address>
    <div class="footer-phone">Tel (52) 33 10 20 30 40</div>
    <address class="footer-contact footer-contact--city" style="font-style:normal">Santa Elena, Jalisco 45210<br>Mexico</address>

    <svg class="ribbon" viewBox="0 0 266 50" aria-hidden="true">
      <defs>
        <linearGradient id="ribbon-fill" x1="0" y1="0" x2="0" y2="1">
          <stop offset="0" stop-color="#3a3a3a"/>
          <stop offset="0.25" stop-color="#080808"/>
          <stop offset="1" stop-color="#000"/>
        </linearGradient>
      </defs>
      <path d="M0 4 L266 4 L252 26 L264 48 L2 48 L14 26 Z" fill="url(#ribbon-fill)"/>
      <path d="M14 6 L252 6" stroke="#9a9a9a" stroke-width="1"/>
    </svg>
    <div class="ribbon__label">Arquitecto</div>
  </footer>
</main>
</body>
</html>
```